Cedar Gate Labradoodle web design

We're a new labradoodle breeder in Charleston, SC in need of a web design.

Our name is Cedar Gate Labradoodles.

Site we like: http://www.pebblefernlabradoodles.example/
http://www.quintbrookdoodles.example/

Logo Font:
The ''Cedar Gate'' font is called TestarossaNF and is available freely at http://www.typevatsample.example/veltrano-kx.font.  The ''Labradoodles'' font is called Worstveld Sling Extra and is available freely at http://www.glyphcrateonline.example/BrimholtDashHeavy.php.

Requirements
Must have
• Our logo
1. Home page
2. Labradoodle F.A.Q.
3. Our doodles
4. Availability
5. Adoption Process
6. Contact us
Link/badge icon for Health Guarantee
Nice to have
• Color and font to match the logo.

An area to add pictures
Should not have
• Rainbows
Rainbow colors

```html
<!DOCTYPE html>
<html lang="en">
<head>
<meta charset="utf-8">
<title>Cedar Gate Labradoodles</title>
<link href="https://fonts.googleapis.com/css2?family=Source+Sans+3:wght@300;400;600&display=swap" rel="stylesheet">
<style>
  :root {
    --cocoa: #2a1607;
    --cocoa-edge: #8b6a4a;
    --cream: #e8dacb;
    --rose: #e27b8d;
    --rose-deep: #c9667a;
    --ink: #5a5452;
    --body-text: #6b6462;
    --hero-text: #4f4c4a;
    --white: #ffffff;
  }
  * { box-sizing: border-box; margin: 0; padding: 0; }
  html, body { width: 1161px; height: 1200px; overflow: hidden; }
  body {
    position: relative;
    background: var(--cream);
    font-family: "Source Sans 3", "Helvetica Neue", Arial, sans-serif;
    color: var(--ink);
  }
  .abs { position: absolute; }

  /* header */
  .site-header { left: 0; top: 0; width: 1161px; height: 611px; background: var(--cocoa); }
  .top-strip { left: 0; top: 0; width: 1161px; height: 8px; background: var(--cocoa-edge); }
  .search { left: 813px; top: 66px; width: 232px; height: 34px; display: flex; }
  .search-field { flex: 1; background: var(--white); }
  .search-button { width: 39px; background: #ececec; display: flex; align-items: center; justify-content: center; }

  .main-nav { left: 116px; top: 146px; width: 929px; height: 51px; background: var(--rose); border-bottom: 5px solid var(--rose-deep); }
  .main-nav a {
    position: absolute; top: 13px; color: var(--white); text-decoration: none;
    font-size: 14px; font-weight: 600; letter-spacing: 0.1px; white-space: nowrap;
  }
  .brand {
    left: 489px; top: 36px; width: 182px; height: 174px; border-radius: 50%;
    background: var(--rose); border: 5px solid var(--cocoa);
    display: flex; align-items: center; justify-content: center; text-align: center;
    color: var(--white); font-size: 19px; font-weight: 600; line-height: 1.2; text-transform: uppercase;
  }

  .hero-photo { left: 117px; top: 197px; width: 927px; height: 347px;
    background:
      linear-gradient(180deg, rgba(60,40,30,0.35) 0%, rgba(60,40,30,0) 30%),
      linear-gradient(100deg, #c9c1b6 0%, #d6cfc5 40%, #ece8e1 62%, #dcd7ce 80%, #a9a99e 100%); }
  .hero-copy { left: 133px; top: 308px; color: var(--hero-text); text-transform: uppercase; white-space: nowrap; }
  .hero-title { font-size: 22px; font-weight: 400; line-height: 28px; }
  .hero-sub { font-size: 16px; font-weight: 400; line-height: 21px; letter-spacing: 0.8px; margin-top: 2px; }
  .shop-button { left: 137px; top: 423px; width: 97px; height: 37px; background: var(--rose);
    color: var(--white); font-size: 15px; font-weight: 600; display: flex; align-items: center; justify-content: center; }
  .slider-dots { left: 554px; top: 572px; }

  /* content */
  .section-title { font-size: 16px; font-weight: 400; text-transform: uppercase; color: var(--ink); white-space: nowrap; }
  .section-title em { font-style: normal; color: var(--rose); }
  .welcome-title { font-size: 15.5px; }
  .lead { left: 115px; top: 669px; width: 291px; font-size: 13.5px; line-height: 18px; color: var(--rose); text-align: justify; }
  .intro { left: 115px; top: 721px; width: 291px; font-size: 11.5px; line-height: 17.5px; color: var(--body-text); text-align: justify; letter-spacing: 0.2px; }
  .tile-photo { width: 291px; height: 148px; }
  .view-all { font-size: 11px; color: var(--rose); text-transform: uppercase; display: flex; align-items: center; gap: 8px; white-space: nowrap; }
  .view-all::after { content: ""; border-left: 5px solid #2a1607; border-top: 4px solid transparent; border-bottom: 4px solid transparent; }
  .frame { width: 291px; height: 147px; background: var(--white); padding: 6px; }
  .frame div { width: 100%; height: 100%; }

  /* footer */
  .site-footer { left: 0; top: 1108px; width: 1161px; height: 92px; background: var(--cocoa); }
  .social { width: 31px; height: 31px; border-radius: 50%; background: var(--rose); top: 1123px; }
  .copyright { left: 117px; top: 1171px; font-size: 10.5px; color: var(--white); white-space: nowrap; }
  .health-badge { left: 919px; top: 1114px; width: 126px; height: 80px; border-radius: 40px;
    background: var(--rose); border: 4px solid var(--white); color: var(--white);
    font-size: 11px; font-weight: 600; line-height: 15px; padding: 20px 0 0 16px; text-transform: uppercase; }
</style>
</head>
<body>
  <header class="site-header abs"></header>
  <div class="top-strip abs"></div>

  <form class="search abs" role="search">
    <div class="search-field"></div>
    <div class="search-button">
      <svg width="14" height="14" viewBox="0 0 14 14"><circle cx="5.5" cy="5.5" r="4" fill="none" stroke="#b9b9b9" stroke-width="2"/><line x1="8.5" y1="8.5" x2="13" y2="13" stroke="#b9b9b9" stroke-width="2.5"/></svg>
    </div>
  </form>

  <nav class="main-nav abs">
    <a style="left:19px">HOME</a>
    <a style="left:92px">LABRADOODLE F.A.Q</a>
    <a style="left:247px">OUR DOODLES</a>
    <a style="left:584px">AVAILABILITY</a>
    <a style="left:691px">ADOPTION PROCESS</a>
    <a style="left:837px">CONTACT US</a>
  </nav>
  <div class="brand abs">Cedar Gate<br>Labradoodles</div>

  <section>
    <div class="hero-photo abs" role="img" aria-label="Photo of a white labradoodle sitting on a carpet"></div>
    <div class="hero-copy abs">
      <p class="hero-title">Finally color comes back into play.<br>Brand new from my shop:</p>
      <p class="hero-sub">Earrings made of 925 silver with a turquoise<br>glass bead and pink glass.</p>
    </div>
    <div class="shop-button abs">SHOP NOW!</div>
    <svg class="slider-dots abs" width="54" height="14" viewBox="0 0 54 14">
      <circle cx="6" cy="6" r="4.5" fill="#e8a25c" stroke="#e08a3c" stroke-width="2"/>
      <circle cx="26" cy="6" r="4.5" fill="none" stroke="#e08a3c" stroke-width="2"/>
      <circle cx="47" cy="6" r="4.5" fill="none" stroke="#e08a3c" stroke-width="2"/>
    </svg>
  </section>

  <main>
    <h2 class="section-title welcome-title abs" style="left:115px;top:629px">Welcome to <em>Cedar Gate Labradoodles</em></h2>
    <p class="lead abs">Sed ut perspiciatis unde omnis iste natus error sit voluptatem accusantium doloremque laudantium,</p>
    <p class="intro abs">Sed ut perspiciatis unde omnis iste natus error sit voluptatem accusantium doloremque laudantium, totam rem aperiam, eaque ipsa quae ab illo inventore veritatis et quasi architecto beatae vitae dicta sunt explicabo. Nemo enim ipsam voluptatem quia voluptas sit aspernatur aut odit aut fugit, sed quia</p>
    <a class="view-all abs" style="left:118px;top:841px">View all</a>

    <h2 class="section-title abs" style="left:435px;top:629px">Availability</h2>
    <div class="tile-photo abs" style="left:435px;top:672px;background:linear-gradient(135deg,#4f8a2e,#a8632c 55%,#6f9a3a)" role="img" aria-label="Photo of a red labradoodle on grass"></div>
    <a class="view-all abs" style="left:435px;top:841px">View all</a>

    <h2 class="section-title abs" style="left:755px;top:629px">Adoption process</h2>
    <div class="tile-photo abs" style="left:755px;top:672px;background:linear-gradient(135deg,#5f9b34,#a4582a 50%,#7dab45)" role="img" aria-label="Photo of a labradoodle puppy on grass"></div>
    <a class="view-all abs" style="left:755px;top:841px">View all</a>

    <h2 class="section-title abs" style="left:115px;top:897px">Our doodles</h2>
    <a class="view-all abs" style="left:982px;top:904px">View all</a>
    <div class="frame abs" style="left:116px;top:931px"><div role="img" aria-label="Photo of a brown labradoodle lying outdoors" style="background:linear-gradient(120deg,#5c4536,#9a7868 50%,#4e3a2e)"></div></div>
    <div class="frame abs" style="left:435px;top:931px"><div role="img" aria-label="Close-up photo of a labradoodle puppy" style="background:linear-gradient(120deg,#4f7a33,#b26c3c 45%,#a8643a 70%,#5b8a3a)"></div></div>
    <div class="frame abs" style="left:755px;top:931px"><div role="img" aria-label="Photo of a golden labradoodle puppy resting" style="background:linear-gradient(120deg,#2c2620,#c18a4a 45%,#a7773e 75%,#3a3028)"></div></div>
  </main>

  <footer class="site-footer abs"></footer>
  <a class="social abs" style="left:116px" aria-label="Social link"></a>
  <a class="social abs" style="left:155px" aria-label="Social link"></a>
  <a class="social abs" style="left:193px" aria-label="Social link"></a>
  <a class="social abs" style="left:232px" aria-label="Social link"></a>
  <p class="copyright abs">© 2013 Cedar Gate Labradoodles &nbsp;|&nbsp; All Rights Reserved.</p>
  <a class="health-badge abs">Health<br>Guarantee</a>
</body>
</html>
```